Harbor Crest Solutions Letterhead Design

The project name sums it up. Just need a professional letterhead design / template we can use in our marketing folders.

Here's the address / contact info for the letterhead: Harbor Crest Solutions 4817 Maple Ridge Dr Suite 150 League City, Texas 77419 346-508-7364 www.harborcrestsolutions.us support@harborcrestsolutions.us

```html
<!DOCTYPE html>
<html lang="en">
<head>
<meta charset="utf-8">
<title>Harbor Crest Solutions Letterhead</title>
<link rel="stylesheet" href="https://fonts.googleapis.com/css2?family=Montserrat:ital,wght@0,400;0,600;0,700;1,400&family=Roboto+Condensed:wght@400&display=swap">
<style>
  :root {
    --backdrop: #e9e7e3;
    --paper: #ffffff;
    --brand-blue: #0a53a3;
    --ink: #3a3a3a;
    --ink-strong: #333333;
    --icon-dark: #2b2b2b;
    --signature-tone: #d9d9d9;
  }
  * { margin: 0; padding: 0; box-sizing: border-box; }
  html, body {
    width: 1200px; height: 908px; overflow: hidden;
    background: var(--backdrop);
  }
  .letterhead {
    position: absolute; left: 266px; top: 22px;
    width: 667px; height: 864px;
    background: var(--paper);
    box-shadow: 0 6px 18px rgba(0,0,0,0.18);
    font-family: "Montserrat", sans-serif;
    color: var(--ink);
    overflow: hidden;
  }
  .brand {
    position: absolute; left: 36px; top: 40px;
    display: flex; align-items: center; gap: 10px;
  }
  .brand-dot {
    width: 40px; height: 40px; border-radius: 50%;
    background: var(--brand-blue);
  }
  .brand-name {
    font-weight: 700; font-size: 22px; color: var(--brand-blue);
    letter-spacing: 0.2px;
  }
  .letter-date {
    position: absolute; left: 91px; top: 292px;
    font-weight: 600; font-size: 12px; color: var(--ink-strong);
  }
  .recipient {
    position: absolute; left: 91px; top: 337px;
    font-size: 12px; line-height: 16.5px;
  }
  .recipient-name { font-weight: 700; color: var(--ink-strong); }
  .recipient-title { font-style: italic; }
  .letter-body {
    position: absolute; left: 91px; top: 420px; width: 490px;
    font-size: 11.6px; line-height: 18.2px;
  }
  .letter-body p + p { margin-top: 15px; }
  .closing {
    position: absolute; left: 476px; top: 686px; width: 110px;
    font-size: 12px;
  }
  .closing-greeting { display: block; text-align: right; }
  .signature-area {
    display: block; margin: 4px 0 0 -5px;
    width: 106px; height: 34px; border-radius: 4px;
    background: var(--signature-tone);
  }
  .signer-name {
    display: block; margin: 4px 0 0 19px;
    font-weight: 700; color: var(--ink-strong);
  }
  .footer-band {
    position: absolute; left: 0; bottom: 0; width: 100%; height: 43px;
    background: var(--brand-blue);
  }
  .contact-row {
    position: absolute; left: 0; top: 813px; width: 100%; height: 24px;
    font-family: "Roboto Condensed", sans-serif; font-size: 7px;
    color: var(--ink-strong); line-height: 10px;
  }
  .contact-item { position: absolute; top: 0; display: flex; gap: 4px; }
  .contact-item svg { width: 18px; height: 18px; flex: none; }
  .contact-item .line-on-band { color: var(--paper); }
  .item-address { left: 36px; }
  .item-phone { left: 235px; }
  .item-web { left: 355px; top: -1px; }
  .item-mail { left: 498px; top: -1px; }
</style>
</head>
<body>
<main class="letterhead">
  <header class="brand">
    <span class="brand-dot"></span>
    <span class="brand-name">Harbor Crest Solutions</span>
  </header>

  <p class="letter-date">Date, 06 March 2022</p>

  <div class="recipient">
    <p>To:</p>
    <p class="recipient-name">Daniel Whitfield</p>
    <p class="recipient-title">Chief Officer</p>
  </div>

  <section class="letter-body">
    <p>Lorem ipsum dolor sit amet, consectetur adipiscing elit. Duis auctor sem vel metus interdum porta. Duis consequat bibendum felis eget cursus. Nulla eget purus vehicula ipsum finibus egestas. Nullam ligula ipsum, mollis sed gravida vitae, maximus eu dolor. Morbi luctus sem a congue consectetur.</p>
    <p>Orci varius natoque penatibus et magnis dis parturient montes, nascetur ridiculus mus. Vestibulum congue eros auctor, ullamcorper libero blandit, tempor tellus. Proin vitae tellus et nunc fringilla lacinia. Sed augue erat, facilisis laoreet velit a, convallis mattis nunc. Nunc sagittis ligula vitae sollicitudin sollicitudin.</p>
    <p>Nulla facilisi. Nulla quis odio vitae purus aliquam fermentum ut nec diam. Fusce sed velit ultrices, aliquam augue ut, sollicitudin orci.</p>
  </section>

  <div class="closing">
    <span class="closing-greeting">Kind Regards</span>
    <span class="signature-area" role="img" aria-label="Handwritten signature"></span>
    <span class="signer-name">Marcus T. Reyes</span>
  </div>

  <div class="footer-band"></div>

  <footer class="contact-row">
    <div class="contact-item item-address">
      <svg viewBox="0 0 18 18"><circle cx="9" cy="9" r="9" fill="var(--icon-dark)"/><path d="M9 3.5a3.3 3.3 0 0 0-3.3 3.3c0 2.5 3.3 7 3.3 7s3.3-4.5 3.3-7A3.3 3.3 0 0 0 9 3.5z" fill="#fff"/><circle cx="9" cy="6.8" r="1.3" fill="var(--icon-dark)"/></svg>
      <div>
        <div>Harbor Crest Solutions 4817 Maple Ridge Dr</div>
        <div class="line-on-band">Suite 150 League City, Texas</div>
      </div>
    </div>
    <div class="contact-item item-phone">
      <svg viewBox="0 0 18 18"><circle cx="9" cy="9" r="9" fill="var(--icon-dark)"/><path d="M6 4.5l1.6 2.4-1 1.1c.7 1.4 1.7 2.4 3.1 3.1l1.1-1 2.4 1.6-.8 1.7c-3.6-.2-6.9-3.5-7.1-7.1z" fill="#fff"/></svg>
      <div>77419 346-508-7364</div>
    </div>
    <div class="contact-item item-web">
      <svg viewBox="0 0 18 18"><circle cx="9" cy="9" r="9" fill="var(--icon-dark)"/><g fill="none" stroke="#fff" stroke-width="0.9"><circle cx="9" cy="9" r="5"/><ellipse cx="9" cy="9" rx="2.2" ry="5"/><path d="M4 9h10M5 6.5h8M5 11.5h8"/></g></svg>
      <div>www.harborcrestsolutions.us</div>
    </div>
    <div class="contact-item item-mail">
      <svg viewBox="0 0 18 18"><circle cx="9" cy="9" r="9" fill="var(--icon-dark)"/><rect x="4.5" y="6" width="9" height="6.2" fill="#fff"/><path d="M4.5 6l4.5 3.6L13.5 6" fill="none" stroke="var(--icon-dark)" stroke-width="0.9"/></svg>
      <div>support@harborcrestsolutions.us</div>
    </div>
  </footer>
</main>
</body>
</html>
```